Need help in designing new business card utilizing our new logo.

Veltrix Solutions works with Construction Business Owners, Managers & IT Professionals to strengthen software usage and increase user productivity.

Our Construction Accounting and Mobile Field Management Software Clients engage with us in the following areas:

New Software Implementations
Software Re-Implementations
Redesigning Software Usage at the User Level
Project Coordination & Management
Continued Software Support

Old tag line:
Weighing Options - Implementing Solutions

www.veltrix-solutions.example

Quad Shift is a product, but not needed for a new business card.

```html
<!DOCTYPE html>
<html lang="en">
<head>
<meta charset="utf-8">
<title>Veltrix Solutions Business Card</title>
<link href="https://fonts.googleapis.com/css2?family=Jost:wght@400;500&family=Open+Sans:wght@600;700&display=swap" rel="stylesheet">
<style>
  :root {
    --backdrop: #3a3a3a;
    --card: #ffffff;
    --brand-blue: #2b2f9c;
    --ink: #2d2d2d;
    --muted: #444444;
  }
  * { box-sizing: border-box; margin: 0; padding: 0; }
  html, body { width: 1200px; height: 800px; overflow: hidden; }
  body {
    background: var(--backdrop);
    font-family: "Jost", sans-serif;
    display: flex;
    flex-direction: column;
    align-items: center;
    justify-content: center;
    gap: 40px;
  }
  .card {
    position: relative;
    width: 520px;
    height: 297px;
    background: var(--card);
    box-shadow: 0 10px 28px rgba(0,0,0,.45);
  }
  .wordmark {
    display: flex;
    align-items: center;
    gap: 10px;
    color: var(--brand-blue);
    font-family: "Jost", sans-serif;
    font-weight: 500;
    letter-spacing: .04em;
    white-space: nowrap;
  }
  .wordmark-square { background: var(--brand-blue); flex: none; }

  /* front */
  .card-front .wordmark {
    position: absolute; left: 50%; top: 120px;
    transform: translateX(-50%);
    font-size: 30px;
  }
  .card-front .wordmark-square { width: 26px; height: 26px; }
  .card-front .site {
    position: absolute; left: 0; right: 0; bottom: 28px;
    text-align: center; font-size: 12px; color: var(--ink);
  }

  /* back */
  .card-back .wordmark {
    position: absolute; right: 34px; top: 38px;
    font-size: 19px;
  }
  .card-back .wordmark-square { width: 16px; height: 16px; }
  .person { position: absolute; left: 40px; top: 92px; }
  .person-name {
    font-family: "Open Sans", sans-serif; font-weight: 700;
    font-size: 21px; color: var(--ink); letter-spacing: .01em;
  }
  .person-title {
    font-family: "Open Sans", sans-serif; font-weight: 600;
    font-size: 13px; color: var(--ink);
  }
  .accent-bar {
    position: absolute; left: 40px; top: 168px;
    width: 28px; height: 3px; background: var(--brand-blue);
  }
  .address {
    position: absolute; left: 40px; top: 190px;
    font-size: 12px; line-height: 1.45; color: var(--muted);
  }
  .contacts {
    position: absolute; left: 40px; top: 226px;
    list-style: none; font-size: 12px; line-height: 1.45; color: var(--muted);
  }
  .contacts li { display: flex; align-items: center; gap: 8px; }
  .contacts svg { width: 11px; height: 11px; flex: none; }
  .web-brand { color: var(--brand-blue); }
</style>
</head>
<body>

  <section class="card card-front">
    <div class="wordmark"><span class="wordmark-square"></span>VELTRIX SOLUTIONS</div>
    <p class="site">www.veltrix-solutions.example</p>
  </section>

  <section class="card card-back">
    <div class="wordmark"><span class="wordmark-square"></span>VELTRIX SOLUTIONS</div>

    <div class="person">
      <h1 class="person-name">DANA R. WHITLOW</h1>
      <p class="person-title">Owner</p>
    </div>

    <div class="accent-bar"></div>

    <p class="address">48 Meridian Avenue - Suite 112<br>Lakeview Falls NY 10001</p>

    <ul class="contacts">
      <li>
        <svg viewBox="0 0 12 12" aria-hidden="true"><path d="M3 1 L5 3.5 L3.8 5 Q5 7.5 7 8.2 L8.5 7 L11 9 L9.5 11 Q2 10 1 2.5 Z" fill="var(--brand-blue)"/></svg>
        800-555-0142 ext.100
      </li>
      <li>
        <svg viewBox="0 0 12 12" aria-hidden="true"><rect x="3" y="0.8" width="6" height="10.4" rx="1" fill="none" stroke="var(--brand-blue)" stroke-width="1.3"/><circle cx="6" cy="9.3" r=".7" fill="var(--brand-blue)"/></svg>
        518-555-0179
      </li>
      <li>
        <svg viewBox="0 0 12 12" aria-hidden="true"><rect x="0.5" y="2" width="11" height="8" fill="var(--brand-blue)"/><path d="M0.5 2 L6 6.5 L11.5 2" fill="none" stroke="#fff" stroke-width="1"/></svg>
        dana.whitlow@veltrix-solutions.example
      </li>
      <li>
        <svg viewBox="0 0 12 12" aria-hidden="true"><circle cx="7" cy="5" r="3.6" fill="none" stroke="var(--brand-blue)" stroke-width="1.4"/><path d="M4.4 7.6 L1 11" stroke="var(--brand-blue)" stroke-width="1.6"/></svg>
        <span>www.<span class="web-brand">veltrix-solutions</span>.example</span>
      </li>
    </ul>
  </section>

</body>
</html>
```